LOLU Baby Massage Classes - flyer to make a difference

I need a single page flyer, preferably single page, to hand out to doctors, medical centres and parents. To also leave on counters of establishments.
It is to promote my baby massage classes. Mums can get together with other mums and book a 5 week course to learn and discover the many benefits of baby massage.
Benefits include: enhances bonding and attachment, understand non-verbal cues from your baby, helps with sleep patterns, help with immune system, increases vagal activity,relief from wind, colic or constipation to name some.

Baby age from birth to 12 months. Group classes or private sessions

I am a Professional Member and Certified by the Global Society of Newborn Touch (GSNT) GSNT Australia is Nationally Accredited and is endorsed by Crown Academy of Carers, the Southern Guild of Birth Attendants, The Southern Union of Daily Living Therapy Australia, The Southern Union of Bodywork Practitioner and is a full member of Wellmind Network Australia.

Class detail and availability contact is Petra Holm 0487 315 208 petra.joanne.holm@quillmail.example www.lolunewborntouch com.au facebook/comLOLUnewborntouch

My colour scheme is green and purple as you will see from my logo and website. I would like my flyer to be softer tones of either both colours or just one.

I will include some images you can choose from or show me any you think will fit in with baby massage. THANK YOU
Updates

Hi The size of my flyer is A6. Approx 150mms x 210mms and single sided. Thank you

Target Market(s)

mums and dads, groups, doctors, midwives

Industry/Entity Type

Medical

Font styles to use
Sans Serif

Colors
87d0c7
b09cc8

Requirements
Must have
• baby photo or photos, both my logo and the GSNT logo. The GSNT logo is to be small
• Baby Massage Classes (wording) is very important to catch the eye.
• Invitation to book a class or gather friends to book is next in importance
• Benefits is next
• The admin information ie.,membership, certification and endorsements are lesser and can be small.
• Contact information to be noticeable.
Nice to have
• If you have an idea, drawing or photo that would look better, please feel free to try it
Should not have
• should not be crowded with information all the same size

```html
<!DOCTYPE html>
<html lang="en">
<head>
<meta charset="utf-8">
<title>LOLU Baby Massage Classes</title>
<link rel="stylesheet" href="https://fonts.googleapis.com/css2?family=Arimo:wght@400;700&display=swap">
<style>
  :root {
    --mint: #a3f3d6;
    --mint-deep: #8fe9c9;
    --lavender: #b09cec;
    --lavender-soft: #b6a3ea;
    --violet: #8a2fdc;
    --green-text: #35cc90;
    --white: #ffffff;
  }
  html, body { margin: 0; padding: 0; overflow: hidden; }
  body { width: 900px; height: 1200px; font-family: "Arimo", Arial, sans-serif; }
  .flyer { position: relative; width: 900px; height: 1200px; overflow: hidden; background: var(--mint); }
  .backdrop { position: absolute; inset: 0; }
  .brand { position: absolute; left: 650px; top: 40px; display: flex; align-items: center; gap: 12px; }
  .brand-dot { width: 86px; height: 86px; border-radius: 50%; background: var(--mint-deep); }
  .brand-name { font-size: 40px; font-weight: 700; color: var(--green-text); letter-spacing: 1px; }
  .headline { position: absolute; left: 30px; top: 160px; margin: 0; font-size: 44px; font-weight: 700; color: var(--violet); }
  .invitation { position: absolute; left: 78px; top: 215px; margin: 0; font-size: 29px; font-weight: 700; color: var(--lavender); line-height: 48px; }
  .invitation span { display: block; }
  .invitation span + span { padding-left: 36px; }
  .benefits-title { position: absolute; left: 62px; top: 366px; margin: 0; font-size: 29px; font-weight: 700; color: var(--green-text); }
  .benefits { position: absolute; left: 0; top: 0; margin: 0; padding: 0; list-style: none; font-size: 24px; font-weight: 700; color: var(--lavender-soft); }
  .benefits li { position: absolute; white-space: nowrap; }
  .partner-mark { position: absolute; left: 32px; top: 622px; display: flex; align-items: center; gap: 8px; }
  .partner-dot { width: 26px; height: 26px; border-radius: 50%; background: var(--violet); opacity: .75; }
  .partner-name { font-size: 18px; font-weight: 700; color: var(--violet); }
  .credentials { position: absolute; left: 30px; top: 706px; width: 390px; margin: 0; font-size: 19px; font-weight: 700; line-height: 26.4px; color: var(--green-text); }
  .contact { position: absolute; left: 30px; top: 1040px; margin: 0; font-style: normal; color: var(--green-text); font-weight: 700; font-size: 19px; line-height: 25px; }
  .contact-name { font-size: 21px; }
  .footer-line { position: absolute; left: 30px; top: 1145px; margin: 0; font-size: 23px; font-weight: 700; color: var(--violet); white-space: nowrap; }
</style>
</head>
<body>
<main class="flyer">
  <svg class="backdrop" width="900" height="1200" viewBox="0 0 900 1200" aria-hidden="true">
    <defs>
      <linearGradient id="photoTone" x1="0" y1="0" x2="1" y2="1">
        <stop offset="0" stop-color="#f4ece6"/>
        <stop offset=".5" stop-color="#e9cdbd"/>
        <stop offset="1" stop-color="#cfd9e6"/>
      </linearGradient>
    </defs>
    <ellipse class="swoosh-band" cx="360" cy="300" rx="640" ry="390" transform="rotate(14 360 300)" fill="var(--lavender)"/>
    <ellipse class="content-oval" cx="330" cy="290" rx="610" ry="355" transform="rotate(14 330 290)" fill="var(--white)"/>
    <path class="accent-curve" d="M470 0 C 700 20 860 90 900 160 L900 120 C 840 50 700 5 560 0 Z" fill="var(--lavender)"/>
    <ellipse class="photo-frame" cx="690" cy="930" rx="330" ry="150" transform="rotate(-8 690 930)" fill="var(--white)"/>
    <ellipse class="photo-frame-inner" cx="700" cy="935" rx="300" ry="128" transform="rotate(-8 700 935)" fill="var(--mint)"/>
  </svg>

  <svg class="photo" width="900" height="1200" viewBox="0 0 900 1200" style="position:absolute;inset:0" role="img" aria-label="Photo of a smiling baby lying on a white towel while an adult's hands massage the baby's chest">
    <ellipse cx="705" cy="938" rx="288" ry="118" transform="rotate(-8 705 938)" fill="url(#photoTone)"/>
  </svg>

  <div class="brand">
    <span class="brand-dot"></span>
    <span class="brand-name">lolu</span>
  </div>

  <h1 class="headline">Baby Massage Classes</h1>
  <p class="invitation"><span>Invitation to book a class or</span><span>gather your friends to book...</span></p>

  <h2 class="benefits-title">Benefits of Baby Massage:</h2>
  <ul class="benefits">
    <li style="left:120px;top:424px">- Enhances bonding and Attachment</li>
    <li style="left:155px;top:470px">- Understand non-verbal cues from your baby</li>
    <li style="left:205px;top:511px">- Relief from wind, colic and constipation</li>
    <li style="left:255px;top:549px">- Helps with sleep patterns</li>
    <li style="left:313px;top:588px">- Helps the immune system</li>
    <li style="left:378px;top:626px">- Increases vagal activity</li>
  </ul>

  <div class="partner-mark">
    <span class="partner-dot"></span>
    <span class="partner-name">GSNT</span>
  </div>

  <p class="credentials">I am a Professional Member and Certified by the Global Society of Newborn Touch (GSNT). GSNT Australia is Nationally Accredited and is endorsed by Crown Academy of Carers and the Southern Guild of Birth Attendants.</p>

  <address class="contact">
    <span class="contact-name">Petra Holm 0487 315 208</span><br>
    petra.joanne.holm@quillmail.example<br>
    www.lolunewborntouch com.au<br>
    facebook/comLOLUnewborntouch
  </address>

  <p class="footer-line">From Birth to 12 Months &nbsp;- &nbsp;Group classes or private sessions</p>
</main>
</body>
</html>
```